TARPLOAD business card design

TARPLOAD is a manufacturer of skip bags supplying both the domestic and commercial market. We wish to convey core characteristics of strength, professionalism and reliability to our customers. We are after a business card that uses our company colours of black and yellow as well as incorporating our logo. Our customers are predominantly in the construction or hardware industry. It is important the cards are professional as we are a small company wishing to appear larger than we actually are. more info on the company and product available at www.tarpload-example.com.au

Target Market(s)

hardware buyers, contruction company owners

Industry/Entity Type

Construction

Requirements
Must have
• company colours of black and yellow - No other colours or variation of yellow black. our company logo. card design must convey "tough"
• Card design must be landscape
• Details to be included on the card are:
• Name and Tiltle
• Phone number : 1300 41 62 53
• Mobile: 0452 718 903
• Fax: 03 9617 4852
• email: dale.hendry@tarpload-example.com.au
• address: PO Box 517, Kelvindale, VIC,3294
• Text in white when on a black background
Nice to have
• I like the idea of the back of the card being black with lighter circle area in the middle with black logo in the centre. Similar to the attached "iconic" card

```html
<!DOCTYPE html>
<html lang="en">
<head>
<meta charset="utf-8">
<title>TARPLOAD business cards</title>
<link href="https://fonts.googleapis.com/css2?family=Source+Sans+3:wght@400;900&display=swap" rel="stylesheet">
<style>
  :root {
    --yellow: #f1cb00;
    --yellow-light: #fbe67a;
    --black: #1a1a1a;
    --ink: #111111;
    --paper: #ffffff;
    --label: #222222;
  }
  * { margin: 0; padding: 0; box-sizing: border-box; }
  html, body { width: 1200px; height: 927px; overflow: hidden; background: var(--paper); }
  body { position: relative; font-family: "Source Sans 3", sans-serif; color: var(--ink); }
  .size-label { position: absolute; left: 15px; top: 12px; font-size: 16px; color: var(--label); }
  .card { position: absolute; width: 366px; height: 237px; background: var(--yellow); overflow: hidden; }
  .front-a { left: 236px; top: 195px; }
  .back-a  { left: 605px; top: 195px; }
  .front-b { left: 236px; top: 522px; }
  .back-b  { left: 605px; top: 522px; }

  .glow { position: absolute; inset: 0;
    background: radial-gradient(ellipse 130px 100px at 50% 40%, var(--yellow-light), var(--yellow)); }
  .band { position: absolute; left: 0; right: 0; background: var(--black); }
  .band-top { top: 0; height: 12px; }
  .band-bottom { bottom: 0; height: 13px; }

  .wordmark { position: absolute; left: 0; right: 0; text-align: center;
    font-weight: 900; color: var(--black); letter-spacing: 0.5px; }
  .front .wordmark { top: 118px; font-size: 40px; line-height: 1; }
  .web { position: absolute; left: 0; right: 0; text-align: center; font-size: 11px; }
  .front-a .web { top: 204px; }
  .front-b .web { top: 215px; }

  .ghost-word { position: absolute; left: -4px; top: 162px; font-size: 76px; font-weight: 900;
    color: var(--black); opacity: 0.06; letter-spacing: 2px; line-height: 1; white-space: nowrap; }

  .mini-mark { position: absolute; left: 14px; top: 28px; font-size: 13px; font-weight: 900; color: var(--black); }
  .person-a { position: absolute; left: 0; right: 0; top: 81px; text-align: center; font-size: 15px; }
  .title-bar { position: absolute; left: 0; right: 0; top: 102px; height: 14px; background: var(--black);
    color: var(--paper); font-size: 10px; text-align: center; line-height: 14px; }

  .row { position: absolute; display: flex; align-items: center; gap: 5px; font-size: 10.5px; white-space: nowrap; }
  .icon { width: 11px; height: 11px; flex: none; fill: var(--black); }
  .at { font-weight: 900; font-size: 12px; width: 11px; text-align: center; line-height: 1; }

  .diagonal { position: absolute; left: 0; top: 0; }
  .person-b { position: absolute; left: 166px; top: 72px; font-size: 15px; color: var(--yellow); }
  .role-b { position: absolute; left: 166px; top: 98px; font-size: 12px; }
  .back-b .row { left: 14px; font-size: 9.5px; gap: 14px; }
</style>
</head>
<body>
  <div class="size-label">85.60 x 53.98 mm</div>

  <!-- Version A front -->
  <section class="card front front-a">
    <div class="glow"></div>
    <div class="band band-top"></div>
    <div class="wordmark">TARPLOAD</div>
    <div class="web">www.tarpload-example.com.au</div>
    <div class="band band-bottom"></div>
  </section>

  <!-- Version A back -->
  <section class="card back-a">
    <div class="mini-mark">TARPLOAD</div>
    <div class="person-a">Dale Hendry</div>
    <div class="title-bar">Managing Director</div>
    <div class="row" style="left:14px;top:173px">
      <svg class="icon" viewBox="0 0 12 12"><path d="M6 1 0 6h2v5h8V6h2z"/></svg>PO Box 517, Kelvindale, VIC,3294
    </div>
    <div class="row" style="left:14px;top:192px">
      <span class="at">@</span>dale.hendry@tarpload-example.com.au
    </div>
    <div class="row" style="left:14px;top:211px">
      <svg class="icon" viewBox="0 0 12 12"><path d="M0 3h12v8H0zM2 5v4h1V5zm2 0v4h1V5zm2 0v4h1V5zm2 0v4h1V5z"/></svg>1300 41 62 53
    </div>
    <div class="row" style="left:140px;top:211px">
      <svg class="icon" viewBox="0 0 12 12"><path d="M3 0h6v12H3zM4 2v5h4V2z"/></svg>0452 718 903
    </div>
    <div class="row" style="left:258px;top:211px">
      <svg class="icon" viewBox="0 0 16 12" style="width:15px"><path d="M3 0h10v4H3zM0 5h16v7H0z"/></svg>03 9617 4852
    </div>
  </section>

  <!-- Version B front -->
  <section class="card front front-b">
    <div class="glow"></div>
    <div class="ghost-word">TARPLOAD</div>
    <div class="wordmark">TARPLOAD</div>
    <div class="web">www.tarpload-example.com.au</div>
  </section>

  <!-- Version B back -->
  <section class="card back-b">
    <svg class="diagonal" width="366" height="237" viewBox="0 0 366 237">
      <polygon points="0,0 366,0 366,94 162,94" fill="var(--black)"/>
    </svg>
    <div class="person-b">Dale Hendry</div>
    <div class="role-b">Managing Director</div>
    <div class="row" style="top:145px">
      <svg class="icon" viewBox="0 0 12 12"><path d="M0 3h12v8H0zM2 5v4h1V5zm2 0v4h1V5zm2 0v4h1V5zm2 0v4h1V5z"/></svg>1300.41.62.53
    </div>
    <div class="row" style="top:162px">
      <svg class="icon" viewBox="0 0 12 12"><path d="M3 0h6v12H3zM4 2v5h4V2z"/></svg>0452.718.903
    </div>
    <div class="row" style="top:179px">
      <svg class="icon" viewBox="0 0 16 12"><path d="M3 0h10v4H3zM0 5h16v7H0z"/></svg>03.9617.4852
    </div>
    <div class="row" style="top:196px">
      <span class="at">@</span>dale.hendry@tarpload-example.com.au
    </div>
    <div class="row" style="top:213px">
      <svg class="icon" viewBox="0 0 12 12"><path d="M6 1 0 6h2v5h8V6h2z"/></svg>PO Box 517, Kelvindale, VIC, 3294
    </div>
  </section>
</body>
</html>
```